Kellow Family Law, legal technician needs a website and design

I need a website for a family law practice. I specialize in collaborative law, unbundled services, and mediation. The website must contain my company logo (file attached), and the website must be a mixture of my personality and my profession. I have attached additional information to explain my personality and profession.

Target Market(s)

Lower through middle-class (income level up to $200,000 per year)

Coding

Coded - Design and coding required

Number of Pages Required

1 page

Requirements
Must have
• Must have enough pages to cover required content. I submitted below some content about the collaborative law process. All of the content is not necessary. However, the website must have enough content to clearly describe the services I offer. Use your professionalism and judgment regarding font, font size, etc.

```html
<!DOCTYPE html>
<html lang="en">
<head>
<meta charset="utf-8">
<title>Kellow Family Law</title>
<link href="https://fonts.googleapis.com/css2?family=Cinzel:wght@400;600;700&family=Cormorant+Garamond:wght@400;500;600&family=Montserrat:wght@400;500&display=swap" rel="stylesheet">
<style>
:root{
  --gold:#b3b13a;
  --gold-dark:#7d7b1c;
  --ink:#111;
  --dark:#1c1c1f;
  --grey-band:#f3f3f3;
  --muted:#555;
  --backdrop:#f6f6f6;
  --white:#fff;
}
*{margin:0;padding:0;box-sizing:border-box}
html,body{width:1200px;height:3886px;overflow:hidden}
body{background:var(--backdrop);font-family:"Cormorant Garamond",serif;color:var(--ink)}
.page{position:absolute;left:113px;top:72px;width:974px;height:3711px;background:var(--white);box-shadow:0 10px 40px rgba(0,0,0,.12);overflow:hidden}
section,header,footer{position:relative;width:974px}
.abs{position:absolute}
.heading{font-family:"Cinzel",serif;font-weight:600;letter-spacing:1px}
.ghost{position:absolute;font-family:"Cinzel",serif;font-weight:700;color:rgba(0,0,0,.08);white-space:nowrap}
.btn{display:inline-block;background:linear-gradient(var(--gold),var(--gold-dark));color:#fff;font-family:"Cormorant Garamond",serif;font-weight:600;text-align:center;border-radius:2px}
.ph{position:absolute}

/* hero */
.hero{height:522px;background:linear-gradient(180deg,#2b3038 0%,#39404a 45%,#22262c 100%);color:#fff}
.hero .photo{inset:0;background:linear-gradient(180deg,rgba(70,80,95,.55),rgba(20,22,26,.7))}
.topbar{font-size:13px;font-family:"Montserrat",sans-serif;color:#ddd}
.nav a{position:absolute;top:48px;font-family:"Montserrat",sans-serif;font-size:11px;color:var(--gold);letter-spacing:.5px;text-decoration:none}
.nav .rule{position:absolute;top:73px;height:1px;background:rgba(255,255,255,.35)}
.brand-mark{left:455px;top:14px;width:66px;height:66px;border:1.5px solid var(--gold);border-radius:50%;display:flex;align-items:center;justify-content:center;text-align:center;font-family:"Cinzel",serif;font-size:9px;color:var(--gold);line-height:1.2}
.hero h1{left:0;width:974px;top:232px;text-align:center;font-family:"Cinzel",serif;font-weight:400;font-size:48px;letter-spacing:1px}
.hero .tag{left:0;width:974px;top:292px;text-align:center;color:var(--gold);font-size:22px}

/* about */
.about{height:438px}
.about p{font-size:13.5px;line-height:1.2;color:#222}

/* services */
.services{height:637px;background:var(--grey-band)}
.card{position:absolute;background:#fff;box-shadow:0 2px 10px rgba(0,0,0,.15);border-radius:3px}
.card h3{font-family:"Cinzel",serif;font-weight:700;font-size:19px}
.card p{font-size:15px;line-height:1.2;color:#444}
.card .go{font-family:"Cinzel",serif;font-weight:700;font-size:13px;color:var(--gold)}

/* mediation */
.mediation{height:336px;background:linear-gradient(90deg,#2a2a2e,#1b1b1e);color:#eee}
.mediation p{font-size:15.5px;line-height:1.15}

/* video */
.video{height:361px}

/* testimonials */
.testimonials{height:472px;background:var(--grey-band)}
.quote{position:absolute;background:#fff;box-shadow:0 2px 10px rgba(0,0,0,.12);border-radius:3px}
.quote p{font-size:12.5px;line-height:1.25;color:#333}
.stars{color:#e2b500;font-size:9px;letter-spacing:1px}

/* experience */
.experience{height:157px;background:#000;color:#fff;text-align:center}

/* articles */
.articles{height:465px}
.article{position:absolute;background:#fff;box-shadow:0 2px 8px rgba(0,0,0,.12)}
.article p{font-size:11px;line-height:1.3;color:#333}
.article .more{font-size:11px;color:var(--gold)}

/* footer */
.footer{height:321px;background:#151515;color:#ddd}
.footer h4{font-family:"Cinzel",serif;font-weight:400;font-size:21px;color:#fff}
.footer li{list-style:none;font-family:"Cinzel",serif;font-size:13px;line-height:26px}
.field{position:absolute;background:#fff;font-family:"Montserrat",sans-serif;font-size:9px;color:#999;padding:5px 6px}
</style>
</head>
<body>
<div class="page">

<header class="hero">
  <div class="ph abs photo" role="img" aria-label="Seattle skyline with the Space Needle under a cloudy sky"></div>
  <div class="abs topbar" style="left:63px;top:15px;display:flex;align-items:center;gap:10px">
    <svg width="14" height="10" viewBox="0 0 14 10"><rect x=".5" y=".5" width="13" height="9" fill="none" stroke="#ddd"/><path d="M.5 .5 7 6 13.5 .5" fill="none" stroke="#ddd"/></svg>hello@kellowlaw.com</div>
  <div class="abs topbar" style="right:77px;top:15px;display:flex;align-items:center;gap:8px">
    <svg width="12" height="12" viewBox="0 0 24 24"><path fill="#fff" d="M6.6 10.8a15 15 0 0 0 6.6 6.6l2.2-2.2c.3-.3.7-.4 1-.2 1.1.4 2.3.6 3.6.6.6 0 1 .4 1 1V20c0 .6-.4 1-1 1A17 17 0 0 1 3 4c0-.6.4-1 1-1h3.5c.6 0 1 .4 1 1 0 1.3.2 2.5.6 3.6.1.3 0 .7-.2 1z"/></svg>555-0142-88</div>
  <nav class="nav">
    <a style="left:62px;color:#fff">HOME</a>
    <div class="abs" style="left:62px;top:67px;width:38px;height:2px;background:#fff"></div>
    <a style="left:130px">ABOUT US</a>
    <a style="left:223px">SERVICE</a>
    <a style="left:308px">PRACTICE AREAS</a>
    <a style="left:560px">ARTICAL</a>
    <a style="left:641px">PROCESS</a>
    <a style="left:724px">MEDIATION</a>
    <a style="left:823px">CONTACT US</a>
    <div class="rule" style="left:62px;width:348px"></div>
    <div class="rule" style="left:563px;width:348px"></div>
  </nav>
  <div class="abs brand-mark">KELLOW<br>FAMILY LAW</div>
  <svg class="abs" style="left:460px;top:176px" width="54" height="44" viewBox="0 0 54 44" fill="none" stroke="#b3b13a" stroke-width="2">
    <path d="M27 4v36M10 10h34M17 42h20M10 10 3 26h14zM44 10l-7 16h14z"/><path d="M3 26a7 4 0 0 0 14 0M37 26a7 4 0 0 0 14 0"/></svg>
  <h1 class="abs">KELLOW FAMILY LAW</h1>
  <div class="abs tag">Collaborative Law And Unbundled Legal Services In King County, Washington State.</div>
  <a class="abs btn" style="left:410px;top:351px;width:152px;height:36px;line-height:36px;font-size:15px">View Practice Areas</a>
  <svg class="abs" style="left:480px;top:450px" width="14" height="26" viewBox="0 0 14 26" fill="none" stroke="#ccc" stroke-width="1.5"><path d="M7 0v24M1 18l6 6 6-6"/></svg>
</header>

<section class="about">
  <div class="ghost" style="left:90px;top:94px;font-size:50px">ABOUT US</div>
  <h2 class="abs heading" style="left:120px;top:106px;font-size:32px">ABOUT US</h2>
  <div class="abs" style="left:120px;top:155px;font-size:19px;line-height:1.15;font-family:'Cinzel',serif">KELLOW FAMILY<br>LAW, <span style="color:var(--gold)">A LEGAL TECHNICIAN</span></div>
  <p class="abs" style="left:120px;top:204px;width:360px">Lorem Ipsum Dolor Sit Amet, Consectetur Adipiscing Elit. Dictumst Pulvinar Pulvinar Urna Proin Sapien Euismod Bibendum Dictum Tristique. Egestas Netus Fermentum Euismod Consequat Tristique Fermentum. Proin Donec Pellentesque Proin Vitae. Sit Ultricies Felis Eget Integer Sed Vitae Lorem Lobortis Pellentesque. Nunc Dui Eget Id Pellentesque Mattis Cum. Sed Mi Et Sollicitudin Iaculis Blandit Varius. A Nulla Vitae Feugiat</p>
  <a class="abs btn" style="left:120px;top:340px;width:92px;height:24px;line-height:24px;font-size:12px">Learn More</a>
  <div class="abs" style="left:600px;top:120px;width:260px;display:flex;align-items:center;gap:14px">
    <div style="width:60px;height:60px;border-radius:50%;background:var(--gold)"></div>
    <div style="font-family:'Cinzel',serif;font-weight:600;font-size:26px;line-height:1.1;color:var(--gold)">Kellow<br>Family Law</div>
  </div>
</section>

<section class="services">
  <div class="ghost" style="left:0;width:974px;text-align:center;top:42px;font-size:58px">SERVICES</div>
  <h2 class="abs heading" style="left:0;width:974px;text-align:center;top:54px;font-size:34px">LEGAL SERVICES PROVIDED</h2>
  <div class="card" style="left:163px;top:132px;width:297px;height:390px">
    <div class="ph" role="img" aria-label="Lawyer and client signing papers beside a gavel" style="left:10px;top:10px;width:277px;height:174px;background:linear-gradient(135deg,#3b2f26,#c9b79a 55%,#e9e4dc)"></div>
    <h3 class="abs" style="left:22px;top:215px">COLLABORATIVE LAW</h3>
    <p class="abs" style="left:22px;top:250px;width:235px">Process In Which The Clients, Along With Their Attorneys, Commit To Seeking A Resolution Of All Issues Without Going To Court Or Threatening To Do So.</p>
    <div class="abs go" style="right:28px;top:356px">GET STARTED</div>
  </div>
  <div class="card" style="left:510px;top:132px;width:297px;height:390px">
    <div class="ph" role="img" aria-label="Courtroom benches with scales of justice" style="left:10px;top:10px;width:277px;height:174px;background:linear-gradient(135deg,#4a2312,#a4552b 50%,#5a2a14)"></div>
    <h3 class="abs" style="left:22px;top:215px">UNBUNDLED SERVICES</h3>
    <p class="abs" style="left:22px;top:250px;width:250px">Lawyer And Client Contract For Specific And Limited Legal Services Without The Lawyer Being Responsible For The Whole Case, I.E. A Parenting Plan.</p>
    <div class="abs go" style="right:22px;top:356px">GET STARTED</div>
  </div>
</section>

<section class="mediation">
  <div class="ph" role="img" aria-label="Dim law library background" style="inset:0;background:linear-gradient(90deg,rgba(60,60,66,.5),rgba(20,20,24,.2))"></div>
  <div class="ghost" style="left:380px;top:46px;font-size:40px;color:rgba(255,255,255,.05)">MEDIATION</div>
  <h2 class="abs heading" style="left:408px;top:52px;font-size:31px;color:var(--gold)">OUR MEDIATION</h2>
  <p class="abs" style="left:408px;top:100px;width:520px">Mediation To Help You Reach An Agreement $250 Per Hour, Available.</p>
  <p class="abs" style="left:408px;top:135px;width:530px">In Addition To The Above Packages, We Offer The Following Services, Which Can Be Adapted To Your Individual Situation: 1</p>
  <p class="abs" style="left:408px;top:187px;width:530px">&nbsp;If You Both Agree And You Have Already Filled Out Your Own Divorce Forms - Divorce Form Review $250 Flat Fee For A One-Time Review, Research, And Recommendations</p>
  <a class="abs btn" style="left:408px;top:257px;width:93px;height:24px;line-height:24px;font-size:12px">Learn More</a>
</section>
<div class="ph" role="img" aria-label="Portrait of a smiling attorney in shirt and tie with arms crossed" style="left:100px;top:1500px;width:213px;height:433px;background:linear-gradient(180deg,#6f5a4c 0%,#c7d4e6 28%,#9fb2cc 70%,#2b2f38 100%);border-radius:90px 90px 0 0"></div>

<section class="video">
  <div class="ph" role="img" aria-label="Video still of a hand writing beside scales of justice" style="left:81px;top:54px;width:359px;height:258px;background:linear-gradient(135deg,#141414,#3a3128 55%,#a08a6b);border-radius:4px"></div>
  <svg class="abs" style="left:240px;top:162px" width="38" height="38" viewBox="0 0 38 38"><circle cx="19" cy="19" r="18" fill="#fff"/><circle cx="19" cy="19" r="12" fill="none" stroke="#b3b13a" stroke-width="2"/><path d="M16 13v12l10-6z" fill="#b3b13a"/></svg>
  <div class="ghost" style="left:485px;top:98px;font-size:50px">VIDEO</div>
  <h2 class="abs heading" style="left:521px;top:115px;font-size:30px">OUR VIDEO</h2>
  <p class="abs" style="left:521px;top:162px;width:350px;font-size:15.5px;line-height:1.15;font-weight:500">Lorem Ipsum Dolor Sit Amet, Consectetur Adipiscing Elit. Sit Venenatis Molestie Sit Cras.</p>
  <a class="abs btn" style="left:521px;top:213px;width:92px;height:25px;line-height:25px;font-size:12px">View More</a>
</section>

<section class="testimonials">
  <div class="ghost" style="left:0;width:974px;text-align:center;top:72px;font-size:52px">TESTIMONIAL</div>
  <h2 class="abs heading" style="left:0;width:974px;text-align:center;top:84px;font-size:31px">OUR TESTIMONIAL</h2>
  <svg class="abs" style="left:72px;top:230px" width="34" height="14" viewBox="0 0 34 14" fill="none" stroke="#b3b13a" stroke-width="1.5"><path d="M34 7H1M7 1 1 7l6 6"/></svg>
  <svg class="abs" style="left:868px;top:230px" width="34" height="14" viewBox="0 0 34 14" fill="none" stroke="#b3b13a" stroke-width="1.5"><path d="M0 7h33M27 1l6 6-6 6"/></svg>

  <div class="quote" style="left:141px;top:153px;width:330px;height:172px">
    <div class="abs" style="left:40px;top:12px;font-family:Georgia,serif;font-size:52px;line-height:1;color:var(--gold)">&ldquo;</div>
    <p class="abs" style="left:30px;top:50px;width:280px;text-indent:52px">Lorem Ipsum Dolor Sit Amet, Consectetur Adipiscing Odio Ultrices Amet, Congue Integer Any Nibh. Amet, Eget Tristique Vitae A Sed Venenatis. Dictumst Eros Id Vitae Orci Id. Senectus Senectus Parturient Any Time Diam, Namtristique Vitae A Sed Venenatis. Dictumst Dictumst Dictumst Eros Id</p>
  </div>
  <svg class="abs" style="left:178px;top:324px" width="40" height="20"><path d="M0 0h40L6 18z" fill="#fff"/></svg>
  <div class="ph" role="img" aria-label="Client portrait" style="left:136px;top:365px;width:52px;height:52px;border-radius:50%;background:linear-gradient(#e7dfd6,#c9b7a6)"></div>
  <div class="abs" style="left:200px;top:370px;font-size:12.5px;line-height:1.1">Lorem Ipsum<br>Lorem Ipsum<div class="stars">★★★★★</div></div>

  <div class="quote" style="left:498px;top:153px;width:333px;height:172px">
    <div class="abs" style="left:40px;top:12px;font-family:Georgia,serif;font-size:52px;line-height:1;color:var(--gold)">&ldquo;</div>
    <p class="abs" style="left:30px;top:50px;width:285px;text-indent:52px">Lorem Ipsum Dolor Sit Amet, Consectetur Adipiscing Odio Ultrices Amet, Congue Integer Any Nibh. Amet, Eget Tristique Vitae A Sed Venenatis. Dictumst Eros Id Vitae Orci Id. Senectus Senectus Parturient Any Time Diam, Namtristique Vitae A Sed Venenatis. Dictumst Dictumst Dictumst Eros Id</p>
  </div>
  <svg class="abs" style="left:535px;top:324px" width="40" height="20"><path d="M0 0h40L6 18z" fill="#fff"/></svg>
  <div class="ph" role="img" aria-label="Client portrait" style="left:495px;top:365px;width:52px;height:52px;border-radius:50%;background:linear-gradient(#8a5a3e,#c99a7a)"></div>
  <div class="abs" style="left:559px;top:370px;font-size:12.5px;line-height:1.1">Lorem Ipsum<br>Lorem Ipsum<div class="stars">★★★★★</div></div>
</section>

<section class="experience">
  <div class="abs" style="left:0;width:974px;top:30px;font-family:'Cinzel',serif;font-size:30px;letter-spacing:1px"><span style="color:var(--gold);font-weight:700">20</span> YEARS OF <span style="color:var(--gold)">EXPERIENCE</span> IN VARIOUS CASES</div>
  <p class="abs" style="left:0;width:974px;top:78px;font-size:15px">Lorem Ipsum Dolor Sit Amet, Consectetur Adipiscing Elit. Sit Venenatis Molestie Sit Cras. Scelerisque Massa</p>
  <div class="abs" style="left:0;width:974px;top:110px;font-family:'Cinzel',serif;font-size:20px;color:var(--gold);display:flex;justify-content:center;align-items:center;gap:20px">GET STARTED <svg width="30" height="12" viewBox="0 0 30 12" fill="none" stroke="#b3b13a" stroke-width="1.5"><path d="M0 6h29M24 1l5 5-5 5"/></svg></div>
</section>

<section class="articles">
  <div class="ghost" style="left:0;width:974px;text-align:center;top:72px;font-size:50px">ARTICALS</div>
  <h2 class="abs heading" style="left:0;width:974px;text-align:center;top:85px;font-size:30px">OUR ARTICALS</h2>
  <div class="article" style="left:155px;top:160px;width:207px;height:236px">
    <div class="ph" role="img" aria-label="Gavel in a wood-panelled courtroom" style="left:6px;top:6px;width:195px;height:112px;background:linear-gradient(135deg,#d8cfc7,#9a3f2a 60%,#4a2014)"></div>
    <p class="abs" style="left:14px;top:133px;width:180px">Em Ipsum Dolor Sit Amet, Consectetur Adipiscing Odio Ultrices Amet, Congue Integer Any Nibh. Amet, Eget Tristique Vitae A Sed Venenatis. Dictumst Eros Id Vitae Orci Id. Senectus</p>
    <div class="abs more" style="right:18px;top:213px">learn more</div>
  </div>
  <div class="article" style="left:386px;top:160px;width:208px;height:236px">
    <div class="ph" role="img" aria-label="Close-up of a wooden gavel" style="left:6px;top:6px;width:196px;height:112px;background:linear-gradient(135deg,#1c120b,#8a5a2e 55%,#c9a26e)"></div>
    <p class="abs" style="left:14px;top:133px;width:180px">Em Ipsum Dolor Sit Amet, Consectetur Adipiscing Odio Ultrices Amet, Congue Integer Any Nibh. Amet, Eget Tristique Vitae A Sed Venenatis. Dictumst Eros Id Vitae Orci Id. Senectus</p>
    <div class="abs more" style="right:18px;top:213px">learn more</div>
  </div>
  <div class="article" style="left:614px;top:160px;width:207px;height:236px">
    <div class="ph" role="img" aria-label="Scales of justice in a courtroom" style="left:6px;top:6px;width:195px;height:112px;background:linear-gradient(135deg,#c86a3a,#6a2a14 55%,#1e1410)"></div>
    <p class="abs" style="left:14px;top:133px;width:180px">Em Ipsum Dolor Sit Amet, Consectetur Adipiscing Odio Ultrices Amet, Congue Integer Any Nibh. Amet, Eget Tristique Vitae A Sed Venenatis. Dictumst Eros Id Vitae Orci Id. Senectus</p>
    <div class="abs more" style="right:18px;top:213px">learn more</div>
  </div>
</section>

<footer class="footer">
  <div class="abs" style="left:82px;top:55px;width:78px;height:78px;border:1.5px solid #fff;border-radius:50%;display:flex;align-items:center;justify-content:center;text-align:center;font-family:'Cinzel',serif;font-size:10px;line-height:1.2;color:#fff">KELLOW<br>FAMILY LAW</div>
  <p class="abs" style="left:52px;top:148px;width:170px;font-size:11px;line-height:1.15">As You Can See, There Are Plenty Of Reasons To Consider Collaborative Practice.</p>
  <h4 class="abs" style="left:240px;top:52px">QUICK LINKS</h4>
  <ul class="abs" style="left:243px;top:91px"><li>HOME</li><li>ABOUT US</li><li>PRACTICE AREAS</li><li>PROCESS</li><li>MEDIATION</li><li>CONTACT US</li></ul>
  <h4 class="abs" style="left:432px;top:52px">CONTACT US</h4>
  <div class="abs" style="left:434px;top:92px;font-size:13px;line-height:1.2">
    <div style="display:flex;gap:14px;margin-bottom:10px"><svg width="13" height="13" viewBox="0 0 24 24"><path fill="#b3b13a" d="M6.6 10.8a15 15 0 0 0 6.6 6.6l2.2-2.2c.3-.3.7-.4 1-.2 1.1.4 2.3.6 3.6.6.6 0 1 .4 1 1V20c0 .6-.4 1-1 1A17 17 0 0 1 3 4c0-.6.4-1 1-1h3.5c.6 0 1 .4 1 1 0 1.3.2 2.5.6 3.6.1.3 0 .7-.2 1z"/></svg>555-0142-88</div>
    <div style="display:flex;gap:14px;margin-bottom:10px"><svg width="14" height="10" viewBox="0 0 14 10"><rect x=".5" y=".5" width="13" height="9" fill="none" stroke="#b3b13a"/><path d="M.5 .5 7 6 13.5 .5" fill="none" stroke="#b3b13a"/></svg>hello@kellowlaw.com</div>
    <div style="display:flex;gap:14px"><svg width="13" height="13" viewBox="0 0 24 24"><path fill="#b3b13a" d="M22 2 2 10l8 3 3 9z"/></svg>Street no 4 near Elm Park ,<br>Seattle USA</div>
  </div>
  <h4 class="abs" style="left:650px;top:48px">GET IN TOUCH</h4>
  <div class="field" style="left:650px;top:88px;width:130px;height:22px">Name</div>
  <div class="field" style="left:793px;top:88px;width:130px;height:22px">Phone number</div>
  <div class="field" style="left:650px;top:120px;width:130px;height:22px">Subject</div>
  <div class="field" style="left:793px;top:120px;width:130px;height:22px">Email</div>
  <div class="field" style="left:650px;top:152px;width:273px;height:50px">Message</div>
  <a class="abs btn" style="left:650px;top:217px;width:90px;height:22px;line-height:22px;font-family:'Montserrat',sans-serif;font-size:10px;font-weight:500">SUBMIT</a>
  <div class="abs" style="left:117px;top:287px;width:740px;height:1px;background:#555"></div>
  <div class="abs" style="left:0;width:974px;top:296px;text-align:center;font-family:'Montserrat',sans-serif;font-size:9px;color:#bbb">COPYRIGHTS © 2021 KELLOW FAMILY LAW. ALL RIGHTS RESERVED. TERMS &amp; CONDITIONS</div>
</footer>

</div>
</body>
</html>
```